Quote Cards With TK May 2025 for Instagram

I would like to put these quotes over one of the pictures attached; Instagram (new size: 4:5 (1080 x 1350 pixels) One Quote per picture, and I want the quote to be bold or easy to read as well. I provided a few reference graphics that I really like as examples below. In very small letters at the bottom add @TKBarlowOnline

All of the pictures are attached; you can pick any photo and add one quote to it; but no stock photography

```html
<!DOCTYPE html>
<html lang="en">
<head>
<meta charset="utf-8">
<title>Quote Cards With TK</title>
<link href="https://fonts.googleapis.com/css2?family=Bebas+Neue&family=Poppins:wght@500&display=swap" rel="stylesheet">
<style>
  :root {
    --page: #ffffff;
    --panel: #b9a7b4;
    --ink: #141114;
    --photo-dark: #2a2528;
    --photo-mid: #5b5157;
  }
  * { margin: 0; padding: 0; box-sizing: border-box; }
  html, body { width: 1200px; height: 3352px; overflow: hidden; background: var(--page); }
  .sheet { position: relative; width: 1200px; height: 3352px; }
  .card {
    position: absolute; width: 495px; height: 618px;
    display: flex; background: var(--panel);
  }
  .col-left { left: 99px; }
  .col-right { left: 607px; }
  .row-1 { top: 101px; } .row-2 { top: 736px; } .row-3 { top: 1371px; }
  .row-4 { top: 2006px; } .row-5 { top: 2641px; }
  .quote-panel {
    position: relative; width: 284px; height: 100%;
    display: flex; align-items: center; justify-content: center;
    padding: 0 8px 90px;
  }
  .quote {
    font-family: "Bebas Neue", "Oswald", sans-serif;
    font-size: 47px; line-height: 1.02; color: var(--ink);
    text-align: center; letter-spacing: 0.2px; font-weight: 400;
  }
  .handle {
    position: absolute; left: 0; right: 0; bottom: 83px;
    text-align: center; font-family: "Poppins", sans-serif;
    font-weight: 500; font-size: 15px; color: var(--ink);
  }
  .photo { flex: 1; height: 100%; }
  .photo-night { background: linear-gradient(180deg, #3b3f52 0%, #1f1c22 60%, #141216 100%); }
  .photo-garden { background: linear-gradient(160deg, #c8b4b8 0%, #b07a92 45%, #8a6a3c 100%); }
  .photo-studio { background: linear-gradient(180deg, #cfcac8 0%, #6b5e60 45%, #1b1a1c 100%); }
  .photo-light { background: linear-gradient(180deg, #d9d6d3 0%, #7a7170 50%, #1e1c1e 100%); }
  .photo-court { background: linear-gradient(180deg, #34384c 0%, #8a6a55 55%, #1d1b1d 100%); }
  .photo-crowd { background: linear-gradient(180deg, #4a3c3a 0%, #8c4f7a 45%, #1c1a1c 100%); }
  .photo-outdoor { background: linear-gradient(180deg, #a9c3dc 0%, #6f7a62 50%, #1b1b1d 100%); }
  .photo-stage { background: linear-gradient(180deg, #7a3c8c 0%, #d0479a 50%, #3a2d6a 100%); }
</style>
</head>
<body>
<main class="sheet">

  <article class="card col-left row-1">
    <div class="quote-panel">
      <p class="quote">Tired. Moody.<br>Stubborn belly<br>fat. Your<br>hormones are<br>screaming<br>for help!<br>Let’s fix that.</p>
      <p class="handle">@TKBarlowOnline</p>
    </div>
    <div class="photo photo-night" role="img" aria-label="Photo of TK in a sheer black top and black jeans in front of a night city window"></div>
  </article>

  <article class="card col-right row-1">
    <div class="quote-panel">
      <p class="quote">That stubborn<br>weight? It’s not<br>your fault.<br>Your hormones<br>are to blame<br>and you’re<br>not alone;<br>but there<br>is a fix.</p>
      <p class="handle">@TKBarlowOnline</p>
    </div>
    <div class="photo photo-garden" role="img" aria-label="Photo of TK in a pink knit outfit among sunflowers and mirrored panels"></div>
  </article>

  <article class="card col-left row-2">
    <div class="quote-panel">
      <p class="quote">Your belly<br>isn’t fat...<br>it’s hormonal.<br>And here’s<br>how to fix it.<br>Comment<br>hormones<br>if nothing<br>is working.</p>
      <p class="handle">@TKBarlowOnline</p>
    </div>
    <div class="photo photo-studio" role="img" aria-label="Photo of TK in a white cropped sweater and black pants"></div>
  </article>

  <article class="card col-right row-2">
    <div class="quote-panel">
      <p class="quote">The stubborn<br>belly fat<br>after 40?<br>It’s not<br>about calories;<br>it’s about<br>your hormones.<br>Here is the fix!</p>
      <p class="handle">@TKBarlowOnline</p>
    </div>
    <div class="photo photo-light" role="img" aria-label="Photo of TK in a sheer striped black top posing by a window"></div>
  </article>

  <article class="card col-left row-3">
    <div class="quote-panel">
      <p class="quote">Flat tummy<br>in your 40s?<br>It’s still<br>possible!<br>Comment<br>bye belly<br>to get the<br>10 secrets to a<br>flatter tummy</p>
      <p class="handle">@TKBarlowOnline</p>
    </div>
    <div class="photo photo-court" role="img" aria-label="Photo of TK in a shimmering brown top on a basketball court"></div>
  </article>

  <article class="card col-right row-3">
    <div class="quote-panel">
      <p class="quote">Bloating.<br>Muffin top.<br>Puffy waistline.<br>Your body’s<br>screaming<br>for a different<br>kind of fix.<br>Here it is</p>
      <p class="handle">@TKBarlowOnline</p>
    </div>
    <div class="photo photo-crowd" role="img" aria-label="Photo of TK courtside in a pink top holding a basketball"></div>
  </article>

  <article class="card col-left row-4">
    <div class="quote-panel">
      <p class="quote">This 90-day plan<br>helped women<br>over 40 slim<br>down, get a<br>tiny waist and<br>feel sexy again.<br>You’re next.</p>
      <p class="handle">@TKBarlowOnline</p>
    </div>
    <div class="photo photo-studio" role="img" aria-label="Photo of TK in a sheer striped black top and high-waist jeans"></div>
  </article>

  <article class="card col-right row-4">
    <div class="quote-panel">
      <p class="quote">You’re doing<br>all the “right”<br>things, but your<br>belly won’t<br>go down?<br>Here’s what you<br>haven’t tried.</p>
      <p class="handle">@TKBarlowOnline</p>
    </div>
    <div class="photo photo-outdoor" role="img" aria-label="Photo of TK in an all-black outfit outdoors against hills and sky"></div>
  </article>

  <article class="card col-left row-5">
    <div class="quote-panel">
      <p class="quote">This is the<br>secret women<br>over 40 are<br>using to<br>get snatched;<br>without starving.<br>Comment skinny<br>to get the<br>exact plan.</p>
      <p class="handle">@TKBarlowOnline</p>
    </div>
    <div class="photo photo-stage" role="img" aria-label="Photo of TK in a pink gown on a colourful event stage"></div>
  </article>

  <article class="card col-right row-5">
    <div class="quote-panel">
      <p class="quote">What worked in<br>your 30s won’t<br>work now.<br>Here’s what<br>actually does.<br>Drop 30 pounds<br>in 3 months.</p>
      <p class="handle">@TKBarlowOnline</p>
    </div>
    <div class="photo photo-light" role="img" aria-label="Photo of TK in a sheer striped black top posing by a window"></div>
  </article>

</main>
</body>
</html>
```